Subway/Bus ad sign for a paid research study

We are looking for someone who can help design an effective advertisement sign for a paid research study. The ad will be displayed in subway stations/bus. The study involves fMRI and is conducted by a laboratory in the University of Kestrelmoor.

We prefer ppt images so we could edit. Dimensions should be 46”h x 60”w, but may vary in the final version depending on our needs.

The way we would like to choose the final design is by running a pretest on friendvale to pick the most attractive ad. Your submission would mean that you consent with this process.

Thank you for your consideration.

Target Market(s)

age 18-64, philadelphia

Requirements
Must have
• The ad must include the following information (we encourage you to come up with better/more catchy slogans)
• - We are looking for participants for a research study
• - This fMRI study is conducted by researchers at University of Kestrelmoor
• - Email KmoorLB7@psy.kestrelmoor-edu.org to see if you are eligible
• - University of Kestrelmoor Logo
• The ad may include the following information
• - Participants get paid up to $190
Nice to have
• original attractive illustrations are highly encouraged.
Should not have
• It seems like brain photos tend to scare people away. Maybe you could focus on using survey-related images or illustrated images of the brain (vs. fMRI scans).

```html
<!DOCTYPE html>
<html lang="en">
<head>
<meta charset="utf-8">
<title>Participants Wanted – fMRI Research Study</title>
<link rel="stylesheet" href="https://fonts.googleapis.com/css2?family=Montserrat:wght@400;600;700;800;900&display=swap">
<style>
  :root {
    --red: #b8322c;
    --red-light: #d0654e;
    --navy: #2e3566;
    --navy-dark: #262c58;
    --teal: #3cc4cc;
    --teal-deep: #1a8a9c;
    --white: #ffffff;
    --accent-red: #b8302e;
    --portrait-warm: #d27a4a;
  }
  * { margin: 0; padding: 0; box-sizing: border-box; }
  html, body { width: 1200px; height: 900px; overflow: hidden; background: var(--navy-dark); }
  .ad {
    position: relative; width: 1200px; height: 900px; overflow: hidden;
    font-family: "Montserrat", Arial, sans-serif; color: var(--white);
  }

  /* Header band */
  .header-band {
    position: absolute; left: 0; top: 0; width: 1200px; height: 330px;
    background: radial-gradient(ellipse at 75% 60%, var(--red-light) 0%, var(--red) 55%, #a82a28 100%);
  }
  .header-frame {
    position: absolute; left: 36px; top: 36px; width: 1130px; height: 294px;
    border: 3px solid var(--navy); border-bottom: none;
  }
  .header-tag {
    position: absolute; left: 358px; top: 14px; width: 480px; height: 92px;
    background: var(--navy); transform: skewX(-4deg);
    display: flex; align-items: center; justify-content: center;
  }
  .header-tag span {
    transform: skewX(4deg); font-size: 44px; font-weight: 400; letter-spacing: 0.5px;
  }
  .headline {
    position: absolute; left: 0; top: 128px; width: 1200px; text-align: center;
    font-size: 100px; font-weight: 800; line-height: 1; letter-spacing: 1px;
  }
  .subhead {
    position: absolute; left: 0; top: 238px; width: 1200px; height: 46px;
    display: flex; align-items: center; justify-content: center; gap: 14px;
    font-size: 38px; font-weight: 700; letter-spacing: 0.5px; line-height: 1;
  }
  .slashes { display: flex; gap: 5px; }
  .slashes i { display: block; width: 5px; height: 30px; transform: skewX(-20deg); background: var(--navy); }

  /* Offer band */
  .offer-band {
    position: absolute; left: 0; top: 330px; width: 1200px; height: 378px;
    background: linear-gradient(100deg, var(--teal-deep) 0%, var(--teal) 40%, #2a6f92 68%, var(--navy) 88%);
    box-shadow: 0 6px 14px rgba(0,0,0,0.35);
  }
  .portrait {
    position: absolute; left: 0; top: 0; width: 444px; height: 378px;
    background: linear-gradient(90deg, #6a3a2a 0%, var(--portrait-warm) 45%, rgba(60,196,204,0) 100%);
  }
  .earn {
    position: absolute; left: 472px; top: 424px; font-size: 96px; font-weight: 900;
    color: var(--navy); line-height: 1; letter-spacing: -1px;
  }
  .earn-note {
    position: absolute; left: 474px; top: 502px; font-size: 34px; font-weight: 400;
    color: var(--navy); line-height: 1.2;
  }
  .amount-label {
    position: absolute; left: 856px; top: 386px; font-size: 32px; font-weight: 600;
    color: var(--navy); line-height: 1.2;
  }
  .amount {
    position: absolute; left: 780px; top: 424px; font-size: 94px; font-weight: 800; line-height: 1;
  }
  .amount-slashes { position: absolute; left: 1030px; top: 426px; display: flex; gap: 14px; }
  .amount-slashes i { width: 11px; height: 84px; background: var(--accent-red); }
  .contact {
    position: absolute; right: 196px; top: 592px; text-align: right;
    font-size: 23px; font-weight: 700; line-height: 1.45;
  }
  .contact a { color: var(--white); text-decoration: underline; text-underline-offset: 4px; }
  .mail-icon { position: absolute; left: 1030px; top: 598px; width: 94px; height: 60px; }

  /* Footer band */
  .footer-band {
    position: absolute; left: 0; top: 708px; width: 1200px; height: 192px;
    background: var(--navy);
  }
  .credit {
    position: absolute; left: 64px; top: 780px; font-size: 24px; line-height: 1.4; font-weight: 400;
  }
  .credit strong { font-weight: 700; }
  .brand {
    position: absolute; left: 832px; top: 764px; display: flex; align-items: center; gap: 16px;
  }
  .brand-mark { width: 70px; height: 70px; background: var(--white); }
  .brand-name { font-size: 32px; font-weight: 600; color: var(--white); line-height: 1; }
</style>
</head>
<body>
<main class="ad">
  <section class="header-band" role="img" aria-label="Red background with faint network of vein-like lines"></section>
  <div class="header-frame"></div>
  <div class="header-tag"><span>We are looking for</span></div>
  <h1 class="headline">PARTICIPANTS</h1>
  <p class="subhead">
    <span class="slashes"><i></i><i></i><i></i></span>
    <span>FOR A fMRI RESEARCH STUDY</span>
    <span class="slashes"><i></i><i></i><i></i></span>
  </p>

  <section class="offer-band">
    <div class="portrait" role="img" aria-label="Portrait of a person in profile overlaid with orange circuit-board lines"></div>
  </section>
  <p class="earn">EARN</p>
  <p class="earn-note">for participation</p>
  <p class="amount-label">UP TO</p>
  <p class="amount">$190</p>
  <div class="amount-slashes slashes"><i></i><i></i><i></i></div>
  <p class="contact">To see if you are eligible, send an email to<br>
    <a href="mailto:KmoorLB7@psy.kestrelmoor-edu.org">KmoorLB7@psy.kestrelmoor-edu.org</a></p>
  <svg class="mail-icon" viewBox="0 0 94 60" aria-hidden="true">
    <rect x="0" y="0" width="94" height="60" rx="4" fill="#ffffff"/>
    <polyline points="3,4 47,36 91,4" fill="none" stroke="#2e3566" stroke-width="4"/>
    <polyline points="3,56 37,30" fill="none" stroke="#2e3566" stroke-width="3"/>
    <polyline points="91,56 57,30" fill="none" stroke="#2e3566" stroke-width="3"/>
  </svg>

  <footer class="footer-band"></footer>
  <p class="credit">This study is conducted by researchers<br>at <strong>University of Kestrelmoor</strong></p>
  <div class="brand">
    <span class="brand-mark"></span>
    <span class="brand-name">Kestrelmoor</span>
  </div>
</main>
</body>
</html>
```